R.T.Pell Logging Web design

Our website needs a redesign. We want it to appear professional and easy to navigate. We will be adding videos and pictures to the new website. We do not sell any products on our website. It should be designed for informational purposes. Our company performs timber harvesting and forest management services. Attached is our new company logo.

www.rtpelllogging-example.com if you want to see our current website.

Industry/Entity Type

Graphic Design

Coding

Coded - Design and coding required

```html
<!DOCTYPE html>
<html lang="en">
<head>
<meta charset="utf-8">
<title>R.T.Pell Logging</title>
<link rel="stylesheet" href="https://fonts.googleapis.com/css2?family=Open+Sans:wdth,wght@75..100,300..800&family=Arimo:wght@400;700&display=swap">
<style>
:root{
  --wood-light:#ecd6b4;
  --wood-mid:#dcb98e;
  --wood-dark:#c99d6c;
  --brown:#5a3311;
  --brown-soft:#7a4a1e;
  --gold:#f2b233;
  --gold-dark:#c98a12;
  --grey-bg:#efefef;
  --white:#ffffff;
  --heading:#3c3c3c;
  --text:#6b6b6b;
  --line:#c9c9c9;
  --field:#e4e4e4;
}
*{margin:0;padding:0;box-sizing:border-box}
html,body{width:1200px;height:2873px;overflow:hidden}
body{position:relative;font-family:"Arimo",Arial,sans-serif;color:var(--text);background:var(--white)}
.abs{position:absolute}

/* hero + header */
.hero{position:absolute;left:0;top:0;width:1200px;height:583px;background:linear-gradient(180deg,var(--wood-light),var(--wood-mid) 70%,var(--wood-dark))}
.header{position:absolute;left:0;top:0;width:1200px;height:92px;background:rgba(240,222,196,.85);border-bottom:1px solid rgba(150,110,60,.35)}
.brand{position:absolute;left:128px;top:24px;display:flex;align-items:center;gap:12px}
.brand-mark{width:44px;height:44px;background:var(--gold);border:3px solid var(--brown)}
.brand-name{font-family:"Open Sans",sans-serif;font-weight:800;font-size:34px;color:var(--brown);letter-spacing:.5px;font-stretch:85%;white-space:nowrap}
.nav{position:absolute;left:408px;top:38px;width:378px;display:flex;justify-content:space-between;font-family:"Open Sans",sans-serif;font-size:12px;font-stretch:90%;color:var(--brown);white-space:nowrap}
.header-social{position:absolute;left:818px;top:36px;display:flex;gap:7px}
.header-social span{width:16px;height:16px;background:var(--gold-dark);border-radius:3px}
.header-phone{position:absolute;left:928px;top:32px;display:flex;align-items:center;gap:8px;font-family:"Open Sans",sans-serif;font-weight:700;font-size:18px;color:var(--brown);white-space:nowrap}
.hero-photo{position:absolute;left:600px;top:92px;width:600px;height:450px;background:radial-gradient(ellipse at 45% 55%,#c99560,#8a5a2c 60%,#5c3a1a);border-radius:0 0 0 40px}
.hero-title{position:absolute;left:128px;top:246px;font-family:"Open Sans",sans-serif;font-stretch:80%;font-weight:700;font-size:30px;line-height:38px;color:var(--brown);white-space:nowrap}
.btn-gold{position:absolute;display:flex;align-items:center;justify-content:center;background:linear-gradient(var(--gold),#e39d1c);border:2px solid var(--brown-soft);border-radius:22px;font-family:"Open Sans",sans-serif;color:var(--brown);font-size:16px;font-weight:600;white-space:nowrap}
.hero-btn{left:128px;top:338px;width:244px;height:42px}
.slider-dots{position:absolute;left:573px;top:553px;display:flex;gap:6px}
.slider-dots span{width:14px;height:14px;border-radius:50%;background:#f4f4f4;border:1px solid #999}
.slider-dots span.active{background:var(--gold-dark)}

/* sections */
.band{position:absolute;left:0;width:1200px}
.band-grey{background:var(--grey-bg)}
.zigzag{position:absolute;left:0;width:1200px;height:12px;background:linear-gradient(-45deg,transparent 8px,var(--c) 0),linear-gradient(45deg,transparent 8px,var(--c) 0);background-size:16px 12px}
.section-title{position:absolute;left:128px;width:944px;display:flex;align-items:center;gap:30px;font-family:"Open Sans",sans-serif;font-weight:700;font-size:26px;color:var(--heading);white-space:nowrap}
.section-title::before,.section-title::after{content:"";flex:1;height:5px;border-top:1px solid var(--line);border-bottom:1px solid var(--line)}
.welcome-text{position:absolute;left:200px;top:718px;width:800px;text-align:center;font-size:12.5px;line-height:21px}

.service{position:absolute;top:1065px;width:280px;text-align:center}
.service-circle{width:170px;height:170px;margin:0 auto;border-radius:50%;background:var(--wood-light);border:2px solid #e6cfae;display:flex;align-items:center;justify-content:center}
.service-photo{width:108px;height:108px;border-radius:50%;background:radial-gradient(#8a9a6a,#4f5e3a)}
.service h3{margin-top:25px;font-family:"Open Sans",sans-serif;font-weight:400;font-size:21px;color:#4a4a4a;white-space:nowrap}
.service p{margin-top:18px;font-size:12.5px;line-height:22px}
.btn-grey{display:inline-block;margin-top:18px;width:130px;height:30px;line-height:28px;border-radius:15px;background:linear-gradient(#f4f4f4,#d4d4d4);border:1px solid #aaa;font-size:12px;color:#444}
.arrow{position:absolute;top:1138px}

.sub-title{position:absolute;font-family:"Open Sans",sans-serif;font-size:20px;color:#555;white-space:nowrap}
.video{position:absolute;left:128px;top:1714px;width:392px;height:256px;background:linear-gradient(135deg,#3e5a2e,#a8733e 50%,#6a4a26)}
.video-bar{position:absolute;left:128px;top:1946px;width:392px;height:22px;background:#e2e2e2;border:1px solid #555}
.thumb{position:absolute;top:1995px;width:80px;height:80px;border:4px solid #fff;background:linear-gradient(135deg,#5e7a3e,#a07040)}
.work{position:absolute;width:146px;height:110px;border:4px solid #fff;background:linear-gradient(135deg,#7a8c56,#a27a4a)}

.form-field{position:absolute;left:128px;width:318px;height:26px;background:var(--field);border:1px solid #d4d4d4;font-size:11px;color:#555;padding:6px 12px}
.form-area{width:359px;height:135px}
.form-btn{left:128px;top:2642px;width:128px;height:32px;font-size:12px}
.info{position:absolute;display:flex;align-items:flex-start;gap:12px;font-size:13px;line-height:20px;color:#666}
.map{position:absolute;left:640px;top:2492px;width:432px;height:180px;border:4px solid #fff;background:linear-gradient(135deg,#dfe7cf,#c8d8b4)}

.footer{position:absolute;left:0;top:2745px;width:1200px;height:128px;background:linear-gradient(180deg,var(--wood-light),var(--wood-mid))}
.copyright{position:absolute;left:128px;top:60px;font-size:12px;color:#333}
.footer-social{position:absolute;left:910px;top:48px;display:flex;gap:10px}
.footer-social span{width:34px;height:34px;border-radius:50%;background:var(--brown-soft)}
</style>
</head>
<body>

<section class="hero">
  <div class="hero-photo" role="img" aria-label="Stack of cut pine logs"></div>
  <header class="header">
    <div class="brand"><span class="brand-mark"></span><span class="brand-name">R.T.Pell</span></div>
    <nav class="nav"><span>HOME</span><span>ABOUT</span><span>SERVICES</span><span>LOCATIONS</span><span>GALLERY</span><span>CONTACT</span></nav>
    <div class="header-social"><span></span><span></span><span></span><span></span></div>
    <div class="header-phone">
      <svg width="24" height="24" viewBox="0 0 24 24"><path fill="#5a3311" d="M6.6 10.8a15 15 0 0 0 6.6 6.6l2.2-2.2c.3-.3.7-.4 1-.2 1.1.4 2.3.6 3.6.6.6 0 1 .4 1 1V20c0 .6-.4 1-1 1A17 17 0 0 1 3 4c0-.6.4-1 1-1h3.5c.6 0 1 .4 1 1 0 1.3.2 2.5.6 3.6.1.3 0 .7-.2 1z"/></svg>
      (555) 014-2277
    </div>
  </header>
  <h1 class="hero-title">RECEIVE HIGH-QUALITY PROFESSIONAL<br>LOGGING &amp; LAND CLEARING SERVICES</h1>
  <div class="btn-gold hero-btn">CALL FOR A FREE ESTIMATE</div>
  <div class="slider-dots"><span></span><span class="active"></span><span></span></div>
</section>

<section class="band band-grey" style="top:583px;height:307px"></section>
<h2 class="section-title" style="top:640px">WELCOME TO R.T.PELL</h2>
<p class="welcome-text">Receive high-quality professional logging and land clearing services, from R.T.Pell Logging Company based in Pine Hollow, TX.<br>Whether your tract is large or small, our team of experts can provide the resources and solutions you need to get the job done right.<br>Our track record for consistency, timely service, and expertise will continue to keep us competitive in the East Texas timber industry.<br>We pay top dollar for your pine and hardwood timber.</p>
<div class="zigzag" style="top:884px;--c:var(--white)"></div>

<h2 class="section-title" style="top:958px">OUR SERVICES</h2>
<svg class="arrow" style="left:126px" width="16" height="28" viewBox="0 0 16 28"><path d="M14 2 3 14l11 12" fill="none" stroke="#cfcfcf" stroke-width="3"/></svg>
<svg class="arrow" style="left:1052px" width="16" height="28" viewBox="0 0 16 28"><path d="M2 2l11 12L2 26" fill="none" stroke="#cfcfcf" stroke-width="3"/></svg>
<div class="service" style="left:134px">
  <div class="service-circle"><div class="service-photo" role="img" aria-label="Harvester machine in a clearing"></div></div>
  <h3>HARVESTING</h3>
  <p>Lorem ipsum dolor sit amet, consectetur adipiscing elit. Sed sit amet varius purus. Duis odio erat, porttitor sit amet lorem sit amet,</p>
  <span class="btn-grey">READ MORE</span>
</div>
<div class="service" style="left:459px">
  <div class="service-circle"><div class="service-photo" role="img" aria-label="Rows of thinned pine plantation trunks"></div></div>
  <h3>PLANTATION THINNING</h3>
  <p>Lorem ipsum dolor sit amet, consectetur adipiscing elit. Sed sit amet varius purus. Duis odio erat, porttitor sit amet lorem sit amet,</p>
  <span class="btn-grey">READ MORE</span>
</div>
<div class="service" style="left:789px">
  <div class="service-circle"><div class="service-photo" role="img" aria-label="Yellow felling head on a machine"></div></div>
  <h3>MECHANICAL FELLING</h3>
  <p>Lorem ipsum dolor sit amet, consectetur adipiscing elit. Sed sit amet varius purus. Duis odio erat, porttitor sit amet lorem sit amet,</p>
  <span class="btn-grey">READ MORE</span>
</div>

<section class="band band-grey" style="top:1490px;height:705px"></section>
<div class="zigzag" style="top:1484px;--c:var(--grey-bg);transform:scaleY(-1)"></div>
<h2 class="section-title" style="top:1566px">OUR GALLERY</h2>
<div class="sub-title" style="left:128px;top:1668px">WATCH VIDEOS</div>
<div class="sub-title" style="left:598px;top:1668px">FEATURED WORK</div>
<div class="video" role="img" aria-label="Video still of stacked cut logs in a forest"></div>
<svg class="abs" style="left:296px;top:1812px" width="56" height="56" viewBox="0 0 56 56"><circle cx="28" cy="28" r="26" fill="rgba(255,255,255,.35)" stroke="#fff" stroke-width="2"/><path d="M22 17l17 11-17 11z" fill="#fff"/></svg>
<div class="video-bar"></div>
<div class="thumb" style="left:128px" role="img" aria-label="Video thumbnail: machine in woods"></div>
<div class="thumb" style="left:230px" role="img" aria-label="Video thumbnail: worker by a tree"></div>
<div class="thumb" style="left:334px" role="img" aria-label="Video thumbnail: cut timber"></div>
<div class="thumb" style="left:436px" role="img" aria-label="Video thumbnail: felling head"></div>

<div class="work" style="left:604px;top:1714px" role="img" aria-label="Worker beside felled log"></div>
<div class="work" style="left:764px;top:1714px" role="img" aria-label="Log loader machine"></div>
<div class="work" style="left:922px;top:1714px" role="img" aria-label="Chainsaw cutting timber"></div>
<div class="work" style="left:604px;top:1838px" role="img" aria-label="Pine plantation rows"></div>
<div class="work" style="left:764px;top:1838px" role="img" aria-label="Worker climbing tree"></div>
<div class="work" style="left:922px;top:1838px" role="img" aria-label="Harvester loading logs"></div>
<div class="work" style="left:604px;top:1962px" role="img" aria-label="Yellow felling head"></div>
<div class="work" style="left:764px;top:1962px" role="img" aria-label="Worker measuring log"></div>
<div class="work" style="left:922px;top:1962px" role="img" aria-label="Chainsaw at work"></div>
<div class="zigzag" style="top:2189px;--c:var(--white)"></div>

<h2 class="section-title" style="top:2275px">CONTACT US</h2>
<div class="sub-title" style="left:128px;top:2362px">GET IN TOUCH</div>
<div class="sub-title" style="left:640px;top:2362px">CONTACT INFORMATION</div>
<div class="form-field" style="top:2411px">Name</div>
<div class="form-field" style="top:2449px">Email</div>
<div class="form-field form-area" style="top:2489px">Type you message here</div>
<div class="btn-gold form-btn">READ MORE</div>

<div class="info" style="left:640px;top:2410px">
  <svg width="18" height="18" viewBox="0 0 24 24"><path fill="#555" d="M6.6 10.8a15 15 0 0 0 6.6 6.6l2.2-2.2c.3-.3.7-.4 1-.2 1.1.4 2.3.6 3.6.6.6 0 1 .4 1 1V20c0 .6-.4 1-1 1A17 17 0 0 1 3 4c0-.6.4-1 1-1h3.5c.6 0 1 .4 1 1 0 1.3.2 2.5.6 3.6.1.3 0 .7-.2 1z"/></svg>
  <span>(555) 014-2277</span>
</div>
<div class="info" style="left:640px;top:2446px">
  <svg width="18" height="18" viewBox="0 0 24 24"><rect x="2" y="5" width="20" height="14" fill="#555"/><path d="M2 5l10 8 10-8" fill="none" stroke="#fff" stroke-width="1.5"/></svg>
  <span>youremail@yoursite.com</span>
</div>
<div class="info" style="left:872px;top:2410px">
  <svg width="16" height="22" viewBox="0 0 16 22"><path fill="#555" d="M8 0a8 8 0 0 0-8 8c0 6 8 14 8 14s8-8 8-14a8 8 0 0 0-8-8zm0 11a3 3 0 1 1 0-6 3 3 0 0 1 0 6z"/></svg>
  <span>PO Box 4410 Pine Hollow,<br>TX 75900 US</span>
</div>
<div class="map" role="img" aria-label="Map showing Pine Hollow, TX location"></div>

<footer class="footer">
  <div class="zigzag" style="top:-6px;--c:var(--white);transform:scaleY(-1)"></div>
  <p class="copyright">Copyright © 2015 R.T.Pell</p>
  <div class="footer-social"><span></span><span></span><span></span><span></span></div>
</footer>

</body>
</html>
```